Calm Fern Healthcare- Aged Care and Community Services

Looking for brochure to advertise our services. I will attach a draft that we do not want to use. Looking for graphics that are as natural as possible to present a personalised service. We supply services to aged people and people with disability. Please make it look classy and professional at the same time. I am looking for creativity. I have also attached the logo. Site addresses can be the last page. ideally looking for 2 designs, one A4 and another smaller possibly DL. Looking for creative out of the box thinkers. Thank you.

Target Market(s)

Aged Care service providers, disability service providers and private hospitals

Font styles to use
Serif
Sans Serif
Script

Colors
6b449b
886aae
eea4c8
f59195
fac994
3176b5
0555a3
cedeed
e4daeb

Requirements
Must have
• Targeted imagery, content and contact details
Nice to have
• personal profiles of people happy with our services

```html
<!DOCTYPE html>
<html lang="en">
<head>
<meta charset="utf-8">
<title>Calm Fern Healthcare Brochure</title>
<link href="https://fonts.googleapis.com/css2?family=Rubik:wght@400;500;700;800&display=swap" rel="stylesheet">
<style>
:root{
  --purple:#6b449b;
  --purple-deep:#5a2f8f;
  --purple-soft:#886aae;
  --lilac:#e4daeb;
  --pink:#e0147a;
  --paper:#f4f3f7;
  --ink:#3a3340;
  --muted:#6a6470;
  --stage:#2b2b2b;
  --white:#ffffff;
}
*{box-sizing:border-box;margin:0;padding:0}
html,body{width:913px;height:1200px;overflow:hidden}
body{background:var(--stage);font-family:"Rubik",Arial,sans-serif;color:var(--ink);position:relative}
.spread{position:absolute;left:66px;width:780px;height:552px;background:var(--paper);overflow:hidden;box-shadow:0 10px 30px rgba(0,0,0,.5)}
.spread--outer{top:28px}
.spread--inner{top:614px}
.fold{position:absolute;left:390px;top:0;width:2px;height:100%;background:rgba(0,0,0,.08)}
.abs{position:absolute}
.photo{position:absolute}
.photo--tinted{background:linear-gradient(135deg,#b9a5d4,#6e4f9c 60%,#3f2a62)}
.photo--garden{background:linear-gradient(135deg,#7fb25a,#c7d9a5 45%,#e8e2d6 60%,#6aa0d0)}
.photo--warm{background:linear-gradient(160deg,#f3e6c9,#b89a7e 55%,#6b5a4e)}
.photo--clinic{background:linear-gradient(160deg,#efe2c4,#d9c7a3 50%,#fafafa)}
.photo--team{background:linear-gradient(160deg,#e6e6ea,#b9a6a0 50%,#8aa2c8)}
.brand{display:flex;align-items:center;gap:10px;font-weight:500}
.brand__dot{width:22px;height:22px;border-radius:50%;flex:none}
.brand--light{color:var(--white);font-size:22px}
.brand--light .brand__dot{background:var(--white)}
.brand--dark{color:var(--purple);font-size:17px}
.brand--dark .brand__dot{background:var(--purple)}
.contact{list-style:none;color:var(--white);font-size:15px;font-weight:500}
.contact li{display:flex;align-items:center;gap:10px;margin-bottom:6px}
.contact svg{width:18px;height:18px;flex:none}
.web{font-size:13px;letter-spacing:.4px;white-space:nowrap}
.web--light{color:var(--white)}
.web--dark{color:var(--purple)}
.headline{color:var(--white);line-height:1.05}
.headline__top{font-size:26px;font-weight:500}
.headline__main{font-size:32px;font-weight:800}
.section-title{font-size:16px;font-weight:700;text-transform:uppercase;letter-spacing:.5px}
.section-title::after{content:"";display:block;width:90px;height:2px;background:currentColor;margin-top:3px}
.box{background:var(--purple);color:var(--white)}
.body-text{font-size:9.5px;line-height:1.35;font-weight:500}
.intro{font-size:12px;font-weight:500;color:var(--muted)}
.about-text{font-size:9px;line-height:1.3;font-weight:500;color:var(--muted)}
.about-text p+p{margin-top:8px}
.list{font-size:11px;line-height:1.35;font-weight:500;padding-left:14px;color:var(--muted)}
.list--small{font-size:7.6px;line-height:1.3;color:var(--white);padding-left:10px}
.criteria-title{font-size:8.5px;font-weight:700;text-transform:uppercase;line-height:1.2}
</style>
</head>
<body>

<section class="spread spread--outer">
  <div class="photo photo--tinted" role="img" aria-label="Carers sharing a card game with elderly residents at an outdoor table, purple tinted" style="left:0;top:0;width:390px;height:310px"></div>
  <svg class="abs" style="left:0;top:0" width="780" height="552" viewBox="0 0 780 552">
    <polygon points="0,320 390,240 390,460 0,500" fill="var(--purple-deep)"/>
    <polygon points="0,500 390,460 390,552 0,552" fill="var(--white)"/>
    <polygon points="20,552 60,525 390,505 390,552" fill="var(--purple)"/>
    <polygon points="390,0 780,0 780,250 390,330" fill="var(--white)"/>
    <polygon points="390,240 560,230 610,300 780,300 780,410 390,440" fill="var(--purple)"/>
    <polygon points="560,235 780,230 780,300 610,300" fill="var(--white)"/>
    <polygon points="390,440 780,410 780,480 390,510" fill="var(--white)"/>
    <polygon points="390,505 780,470 780,552 390,552" fill="var(--purple)"/>
    <line x1="545" y1="232" x2="780" y2="222" stroke="var(--pink)" stroke-width="4"/>
  </svg>
  <div class="photo photo--garden" role="img" aria-label="Smiling carer high-fiving an elderly woman in a garden" style="left:390px;top:0;width:390px;height:228px"></div>

  <div class="brand brand--light abs" style="left:40px;top:352px"><span class="brand__dot"></span>Calm Fern Healthcare</div>
  <ul class="contact abs" style="left:40px;top:392px">
    <li><svg viewBox="0 0 24 24"><path d="M12 2a7 7 0 0 0-7 7c0 5 7 13 7 13s7-8 7-13a7 7 0 0 0-7-7zm0 9.5a2.5 2.5 0 1 1 0-5 2.5 2.5 0 0 1 0 5z" fill="#fff"/></svg>14 Wattle Grove, Harlow WA 6120</li>
    <li><svg viewBox="0 0 24 24"><rect x="3" y="5" width="18" height="14" rx="2" fill="none" stroke="#fff" stroke-width="2"/><path d="M3 7l9 6 9-6" fill="none" stroke="#fff" stroke-width="2"/></svg>admin@calmfernhealthcare.com.au</li>
    <li><svg viewBox="0 0 24 24"><path d="M6.6 10.8a15 15 0 0 0 6.6 6.6l2.2-2.2a1 1 0 0 1 1-.25 11 11 0 0 0 3.6.6 1 1 0 0 1 1 1V20a1 1 0 0 1-1 1A17 17 0 0 1 3 4a1 1 0 0 1 1-1h3.5a1 1 0 0 1 1 1 11 11 0 0 0 .6 3.6 1 1 0 0 1-.25 1z" fill="#fff"/></svg>08 9000 4127</li>
  </ul>
  <div class="web web--dark abs" style="left:110px;top:488px;transform:rotate(-5deg)">www.calmfernhealthcare.com.au</div>

  <div class="headline abs" style="left:410px;top:320px;transform:rotate(-5deg)">
    <div class="headline__top">Reimagining</div>
    <div class="headline__main">Healthcare</div>
  </div>
  <div class="brand brand--dark abs" style="left:610px;top:252px"><span class="brand__dot"></span>Calm Fern<br>Healthcare</div>
  <div class="web web--dark abs" style="left:540px;top:458px;transform:rotate(-5deg)">www.calmfernhealthcare.com.au</div>
  <div class="fold"></div>
</section>

<section class="spread spread--inner">
  <svg class="abs" style="left:0;top:0" width="780" height="552" viewBox="0 0 780 552">
    <polygon points="0,520 60,500 390,500 390,552 0,552" fill="var(--purple)"/>
    <polygon points="390,505 780,505 780,552 390,552" fill="var(--purple)"/>
  </svg>

  <div class="box abs" style="left:40px;top:20px;width:300px;height:160px;padding:14px 16px">
    <h2 class="section-title">Services</h2>
    <p class="body-text" style="margin-top:8px">Our mission is to supply values driven, responsive, conscientious, and responsible personnel to the aged care sector, disability services, private and public health sectors. Our passion for human services and experience in recruitment enables us to attract exceptional people with great values ready and willing to make a difference to the lives of vulnerable people.</p>
  </div>
  <p class="intro abs" style="left:50px;top:192px;width:230px">We have a comprehensive database of the following personnel</p>
  <ul class="list abs" style="left:50px;top:232px;width:230px">
    <li>Registered Nurses (Aged Care, Disability, Emergency, Public and Private healthcare)</li>
    <li>Clinical Nurses</li>
    <li>Nurse Practitioners</li>
    <li>Enrolled Nurses</li>
    <li>Assistants in Nursing (Carers/ PCA's)</li>
    <li>Support Workers (Disability, Community and Mental health)</li>
    <li>Healthcare Endorsed Chefs and Cooks</li>
    <li>Catering Assistants</li>
    <li>Kitchen hands</li>
    <li>Cleaners</li>
  </ul>
  <div class="web web--light abs" style="left:90px;top:518px">www.calmfernhealthcare.com.au</div>

  <div class="photo photo--warm" role="img" aria-label="Smiling elderly woman walking with support" style="left:300px;top:192px;width:140px;height:290px"></div>
  <div class="photo photo--clinic" role="img" aria-label="Nurse in white uniform speaking with a resident" style="left:440px;top:30px;width:135px;height:220px"></div>

  <h2 class="section-title abs" style="left:588px;top:22px;color:var(--purple)">About Us</h2>
  <div class="about-text abs" style="left:588px;top:50px;width:182px">
    <p>Calm Fern Healthcare is a staffing provider with a contemporary approach to recruiting and placing exceptional people in human services. We maintain a comprehensive database of General Registered Nurses, Enrolled Nurses, Nursing Assistants, Medication Competent Nursing Assistants, Chefs, Cooks, Catering Assistants, Kitchen hands, Laundry and Cleaning staff. Our staff are skilled in Aged Care, Disability Services, Community Care, Public and Private Healthcare.</p>
    <p>Our vision is to be the most responsive staffing agency in Australia.</p>
  </div>

  <div class="box abs" style="left:450px;top:268px;width:320px;height:222px"></div>
  <div class="photo photo--team" role="img" aria-label="Group of smiling care staff" style="left:460px;top:278px;width:140px;height:202px"></div>
  <div class="abs" style="left:608px;top:280px;width:158px;color:var(--white)">
    <p class="criteria-title">All staff must meet the following benchmark criteria</p>
    <ul class="list list--small" style="margin-top:5px">
      <li>6 months relevant industry experience in Australia</li>
      <li>National police clearance under 6 months old (must have unsupervised contact for vulnerable groups)</li>
      <li>Qualifications and registrations e.g. Certificate III Individual Support or AHPRA registration</li>
      <li>Excellent communication skills</li>
      <li>A genuine passion for people's health and wellbeing</li>
      <li>A reliable vehicle and state issued drivers licence</li>
      <li>An understanding of quality and safety outcomes for healthcare providers</li>
      <li>Flexibility and adaptability</li>
    </ul>
  </div>
  <div class="web web--light abs" style="left:490px;top:518px">www.calmfernhealthcare.com.au</div>
  <div class="fold"></div>
</section>

</body>
</html>
```